Lumindo Business Card

Need a business card for our business.

Attached are our Logos. There is either the white and black all the all red with white. Either Logo can be used.

The winner will be provided the details for phone number and address.

Good Luck!

Business

```html
<!DOCTYPE html>
<html lang="en">
<head>
<meta charset="utf-8">
<title>Lumindo Business Card</title>
<link rel="stylesheet" href="https://fonts.googleapis.com/css2?family=Cinzel:wght@500&family=Questrial&display=swap">
<style>
  :root {
    --backdrop: #161616;
    --card-white: #ffffff;
    --card-shade: #ececec;
    --band-black: #0c0c0c;
    --brand-red: #8e1c1f;
    --ink-dark: #1f1f1f;
    --ink-mid: #3a3a3a;
    --band-text: #d6d6d6;
  }
  * { margin: 0; padding: 0; box-sizing: border-box; }
  html, body {
    width: 1200px; height: 871px; overflow: hidden;
    background: var(--backdrop);
  }
  .stage { position: relative; width: 1200px; height: 871px; }

  .card {
    position: absolute;
    width: 600px; height: 343px;
    background: linear-gradient(160deg, var(--card-white) 55%, var(--card-shade));
    overflow: hidden;
  }
  .card--back { left: 80px; top: 70px; }
  .card--front { left: 520px; top: 460px; }

  .brand-name {
    font-family: "Questrial", sans-serif;
    color: var(--brand-red);
    font-weight: 400;
    text-transform: uppercase;
    line-height: 1;
    text-align: center;
  }
  .brand-name__word { display: block; font-size: 50px; letter-spacing: 2px; }
  .brand-name__sub { display: block; font-size: 16px; letter-spacing: 9px; margin-top: 6px; }

  .card--back .brand-name {
    position: absolute; left: 0; right: 0; top: 128px;
  }

  .card--front .brand-name {
    position: absolute; left: 40px; top: 92px; width: 230px;
  }
  .card--front .brand-name__word { font-size: 44px; }
  .card--front .brand-name__sub { font-size: 14px; letter-spacing: 8px; }

  .contact {
    position: absolute; left: 330px; top: 70px;
    font-family: "Questrial", sans-serif;
    color: var(--ink-mid);
  }
  .contact__name {
    font-family: "Cinzel", serif;
    font-size: 19px; letter-spacing: 2px; color: var(--ink-dark);
  }
  .contact__role { font-size: 14px; color: var(--brand-red); letter-spacing: 1px; margin-top: 1px; }
  .contact__address { margin-top: 22px; font-size: 14px; line-height: 1.3; letter-spacing: 1.2px; }
  .contact__phones { margin-top: 14px; font-size: 14px; letter-spacing: 1.5px; }
  .contact__line { display: flex; align-items: center; gap: 16px; height: 20px; }
  .contact__line svg { width: 12px; height: 12px; fill: var(--brand-red); }

  .card__band {
    position: absolute; left: 0; right: 0; bottom: 0; height: 78px;
    background: var(--band-black);
  }
  .card__web {
    position: absolute; left: 140px; bottom: 28px;
    font-family: "Questrial", sans-serif; font-size: 14px;
    letter-spacing: 2.5px; color: var(--band-text);
  }
</style>
</head>
<body>
<main class="stage">
  <section class="card card--back" aria-label="Card back">
    <p class="brand-name">
      <span class="brand-name__word">Lumindo</span>
      <span class="brand-name__sub">Industries</span>
    </p>
  </section>

  <section class="card card--front" aria-label="Card front">
    <p class="brand-name">
      <span class="brand-name__word">Lumindo</span>
      <span class="brand-name__sub">Industries</span>
    </p>

    <div class="contact">
      <p class="contact__name">Marek Olsen</p>
      <p class="contact__role">Director</p>
      <p class="contact__address">address<br>87 harbor lane<br>eastvale, ST 55012</p>
      <div class="contact__phones">
        <p class="contact__line">
          <svg viewBox="0 0 12 12" aria-hidden="true"><path d="M1 4c0-2 2-3 5-3s5 1 5 3v1H8V4H4v1H1z M3 6h6l1 5H2z"/></svg>
          <span>555-204-3180</span>
        </p>
        <p class="contact__line">
          <svg viewBox="0 0 12 12" aria-hidden="true"><path d="M3 1h6v3H3z M1 5h10v5H9V8H3v2H1z M3 9h6v2H3z"/></svg>
          <span>555-204-3181</span>
        </p>
      </div>
    </div>

    <div class="card__band">
      <p class="card__web">www.lumindoworks.com</p>
    </div>
  </section>
</main>
</body>
</html>
```